Restwell Path App - Featured Graphics/Screenshots and Icon

We need graphics for a new app that is a step-by-step program for treating insomnia.
What is needed:
1) app icon (1024x1024 so it can be scaled down)
2) general featured image for use in advertising and app stores
3) screenshots incorporating text (Based on Cognitive Behavioral Therapy for Insomnia, An Innovative and Interactive Self-Help Program, Recommendations Tailored to Your Sleep Patterns, Track Your Sleep).
We have included a variety of example screenshots from the app.
Example text to include with screenshots and/or feature graphics.
1. Based on Cognitive Behavioral Therapy for Insomnia (CBT-I)
2. CBT-I is recommended as a wise choice by buyer digest and a first-line treatment approach by the Federal Bureau of Wellness (FBW)
3. An Innovative and Interactive Self-Help Program
4. Recommendations Tailored to Your Sleep Patterns
5. Track Your Sleep
Here is an overview of the program:
The Restwell Path is an app developed to enable more access to cognitive-behavior therapy for insomnia (CBT-I). CBT-I is recognized as a first line treatment approach by the Federal Bureau of Wellness, however there are few trained providers of the treatment. The Restwell Path will guide you through the cognitive-behavioral treatment process in a step-by-step manner. You will be introduced to new steps on a weekly basis. The first step is to establish a baseline using sleep logs. This is very important as the information gathered will be used to set your initial sleep/wake schedule. Following this initial step, you will be guided through a process of re-establishing a natural drive to sleep, resetting your circadian rhythm, learning to recognize/manage anxiety, apply productive ways to think about sleep, and ways to prevent relapse. The treatment approach can be challenging. It will require completion of all tasks and maintaining the recommended sleep schedule.
We prefer layered PSD files to allow for easy scaling and / or alteration.
Target Market(s)
Mobile app users with insomnia.
Look and feel

```html
<!DOCTYPE html>
<html lang="en">
<head>
<meta charset="utf-8">
<title>Restwell Path – Welcome</title>
<link rel="stylesheet" href="https://fonts.googleapis.com/css2?family=Raleway:wght@500&family=Open+Sans:wght@400&display=swap">
<style>
  :root {
    --sky: #4eb1dd;
    --white: #ffffff;
    --button-text: #3aa5d6;
    --button-shadow: #a9cfe2;
  }
  * { box-sizing: border-box; margin: 0; padding: 0; }
  html, body {
    width: 677px;
    height: 1200px;
    overflow: hidden;
    background: var(--sky);
  }
  .screen {
    position: relative;
    width: 677px;
    height: 1200px;
    background: var(--sky);
    color: var(--white);
    font-family: "Raleway", sans-serif;
  }
  .status-bar {
    position: absolute;
    top: 0; left: 0; right: 0;
    height: 44px;
    display: flex;
    align-items: center;
    justify-content: space-between;
    padding: 0 14px;
    font-family: "Open Sans", sans-serif;
    font-size: 24px;
    color: var(--white);
  }
  .status-left, .status-right {
    display: flex;
    align-items: center;
    gap: 10px;
  }
  .signal { display: flex; gap: 4px; }
  .signal span {
    width: 11px; height: 11px; border-radius: 50%;
    background: var(--white);
  }
  .signal span.empty { background: none; border: 1.5px solid var(--white); }
  .brand-mark {
    position: absolute;
    left: 260px;
    top: 104px;
    width: 190px;
    height: 190px;
    border-radius: 50%;
    border: 7px solid var(--white);
  }
  .app-name {
    font-family: "Raleway", sans-serif;
    font-weight: 500;
    font-size: 104px;
    line-height: 1;
    color: var(--white);
  }
  .app-name span {
    position: absolute;
    white-space: nowrap;
  }
  .app-name .line-one { left: 112px; top: 301px; }
  .app-name .line-two { left: 372px; top: 509px; }
  .auth-button {
    position: absolute;
    left: 253px;
    width: 172px;
    height: 172px;
    border-radius: 50%;
    background: var(--white);
    box-shadow: 9px 9px 0 var(--button-shadow);
    display: flex;
    align-items: center;
    justify-content: center;
    font-family: "Raleway", sans-serif;
    font-weight: 500;
    font-size: 32px;
    letter-spacing: 1px;
    color: var(--button-text);
    text-decoration: none;
  }
  .auth-button.log-in { top: 632px; }
  .auth-button.sign-up { top: 898px; }
</style>
</head>
<body>
<main class="screen">
  <header class="status-bar">
    <div class="status-left">
      <div class="signal">
        <span></span><span></span><span></span><span></span><span class="empty"></span>
      </div>
      <span class="carrier">NORTHWAVE</span>
      <svg class="wifi-icon" width="28" height="22" viewBox="0 0 28 22" aria-hidden="true">
        <path d="M2 8 A17 17 0 0 1 26 8" fill="none" stroke="#fff" stroke-width="3" stroke-linecap="round"/>
        <path d="M7 13 A10 10 0 0 1 21 13" fill="none" stroke="#fff" stroke-width="3" stroke-linecap="round"/>
        <circle cx="14" cy="18" r="3" fill="#fff"/>
      </svg>
    </div>
    <div class="status-right">
      <span class="battery-level">82%</span>
      <svg class="battery-icon" width="64" height="24" viewBox="0 0 64 24" aria-hidden="true">
        <rect x="1.5" y="2.5" width="46" height="19" rx="4" fill="none" stroke="#fff" stroke-width="2"/>
        <rect x="4.5" y="5.5" width="36" height="13" rx="2" fill="#fff"/>
        <rect x="49" y="8" width="3" height="8" rx="1" fill="#fff"/>
        <path d="M60 2 L55 13 H59 L57 22 L63 10 H59 Z" fill="#fff"/>
      </svg>
    </div>
  </header>

  <div class="brand-mark" aria-hidden="true"></div>
  <h1 class="app-name">
    <span class="line-one">Restwell</span>
    <span class="line-two">Path</span>
  </h1>

  <a class="auth-button log-in" href="#">LOG IN</a>
  <a class="auth-button sign-up" href="#">SIGN UP</a>
</main>
</body>
</html>
```